Networking card

I just need a simple design with the following information:
Ravin Doshu
318.647.2094
rdoshu583016@mailvanta.com

I would like to have a white background with blue text like in this sample: https://cardmintly.com/business-card-207346/

```html
<!DOCTYPE html>
<html lang="en">
<head>
<meta charset="utf-8">
<title>Ravin Doshu — Business Card</title>
<link rel="stylesheet" href="https://fonts.googleapis.com/css2?family=Saira:wght@400;500;700&display=swap">
<style>
  :root {
    --page-bg: #ececec;
    --card-bg: #ffffff;
    --ink: #1b4a6b;
    --rule: #cfd6dc;
  }
  * { box-sizing: border-box; margin: 0; padding: 0; }
  html, body {
    width: 1200px;
    height: 1200px;
    overflow: hidden;
    background: var(--page-bg);
  }
  body {
    display: flex;
    align-items: center;
    justify-content: center;
    font-family: "Saira", sans-serif;
  }
  .business-card {
    position: relative;
    width: 1050px;
    height: 600px;
    background: var(--card-bg);
    box-shadow: 0 2px 8px rgba(0,0,0,0.08);
  }
  .card-frame {
    position: absolute;
    inset: 42px 40px 42px 34px;
    border: 5px solid var(--ink);
  }
  .card-content {
    position: absolute;
    inset: 0;
    display: flex;
    flex-direction: column;
    align-items: center;
    justify-content: center;
    color: var(--ink);
    text-align: center;
    padding-bottom: 30px;
  }
  .person-name {
    font-weight: 700;
    font-size: 49px;
    letter-spacing: 2px;
    line-height: 1;
  }
  .person-title {
    font-weight: 500;
    font-size: 29px;
    letter-spacing: 1px;
    margin-top: 10px;
  }
  .contact-divider {
    display: flex;
    align-items: center;
    gap: 8px;
    margin: 22px 0 22px;
  }
  .divider-line {
    width: 50px;
    height: 2px;
    background: var(--rule);
  }
  .contact-icon { width: 40px; height: 40px; display: block; }
  .contact-line {
    font-weight: 500;
    font-size: 34px;
    letter-spacing: 1px;
    line-height: 1.2;
  }
</style>
</head>
<body>
  <article class="business-card">
    <div class="card-frame"></div>
    <div class="card-content">
      <h1 class="person-name">RAVIN DOSHU</h1>
      <p class="person-title">President</p>
      <div class="contact-divider">
        <span class="divider-line"></span>
        <svg class="contact-icon" viewBox="0 0 40 40" aria-label="Phone">
          <circle cx="20" cy="20" r="20" fill="var(--ink)"/>
          <path d="M13 11c1-1 2-1 3 0l3 4c.6.9.4 1.8-.3 2.5l-1.3 1.2c1 2 2.6 3.6 4.6 4.6l1.2-1.3c.7-.7 1.6-.9 2.5-.3l4 3c1 1 1 2 0 3l-2 2c-1.5 1.2-4 1-7-1-3.5-2.3-6.4-5.2-8.7-8.7-2-3-2.2-5.5-1-7z" fill="#fff"/>
        </svg>
        <svg class="contact-icon" viewBox="0 0 40 40" aria-label="Email">
          <circle cx="20" cy="20" r="20" fill="var(--ink)"/>
          <rect x="10" y="13" width="20" height="14" rx="1.5" fill="none" stroke="#fff" stroke-width="2"/>
          <path d="M11 14l9 7 9-7" fill="none" stroke="#fff" stroke-width="2"/>
          <path d="M11 26l6-5M29 26l-6-5" fill="none" stroke="#fff" stroke-width="1.5"/>
        </svg>
        <span class="divider-line"></span>
      </div>
      <p class="contact-line">318.647.2094</p>
      <p class="contact-line">rdoshu583016@mailvanta.com</p>
    </div>
  </article>
</body>
</html>
```